THE VELVET SPARROWS DANCE CONCERT

Hello again! We need a Front Cover for our Dance Showcase Program. Our theme is year is "LEGENDS" .
We are paying Tribute to the Musical Legends through the years. ORLAN, DORIAN WEXFORD, KESTRO, MISS ZUZU etc.
It should include:
1. our Name and Logo (three girls) , which we will provide.
2. Colorful and Bright, Flashy SUPERSTAR feel to it!
3. Size for Print is 8.25 by 10.75 (front page of a magazine type booklet)
4.It should Say somewhere:
" The Velvet Sparrows Dance Factory presents... "
LEGENDS
5. include "2023 Annual Showcase"
6. Include our website address somewhere : www.VSDFstudios-demo.net
7: include " Follow us @VSDF (Snapvale Logo)
you have been working with us for a few years now. Thank you for sharing your gifts and art!
Music Lovers
Entertainment

```html
<!DOCTYPE html>
<html lang="en">
<head>
<meta charset="UTF-8">
<title>Legends – 2023 Annual Showcase</title>
<link rel="stylesheet" href="https://fonts.googleapis.com/css2?family=Anton&family=Great+Vibes&family=Poppins:wght@500;600;700;800&display=swap">
<style>
  :root {
    --plum-top: #5e0c6a;
    --magenta: #b3136e;
    --crimson: #8a0f3c;
    --wine: #3d0a2c;
    --night: #0b0418;
    --white: #ffffff;
    --lime: #d6e31b;
    --neon-green: #3fe07a;
    --neon-violet: #b98cff;
    --neon-pink: #e52fe0;
    --silver-hi: #ffffff;
    --silver-lo: #8c8c94;
  }
  * { margin: 0; padding: 0; box-sizing: border-box; }
  html, body {
    width: 900px; height: 1200px; overflow: hidden;
    background: var(--night);
  }
  .cover {
    position: relative;
    width: 900px; height: 1200px; overflow: hidden;
    background:
      radial-gradient(ellipse 520px 240px at 50% 300px, rgba(255,60,140,.5), transparent 70%),
      linear-gradient(180deg, var(--plum-top) 0%, var(--magenta) 18%, var(--crimson) 32%, var(--wine) 55%, #2a0a2e 80%, var(--night) 100%);
    font-family: 'Poppins', sans-serif;
    color: var(--white);
    text-align: center;
  }
  .spotlights {
    position: absolute; inset: 0 0 auto 0; height: 380px;
    background:
      linear-gradient(155deg, transparent 30%, rgba(255,190,255,.26) 34%, transparent 40%),
      linear-gradient(205deg, transparent 30%, rgba(255,190,255,.26) 34%, transparent 40%),
      linear-gradient(140deg, transparent 40%, rgba(255,120,170,.2) 44%, transparent 50%),
      linear-gradient(220deg, transparent 40%, rgba(255,120,170,.2) 44%, transparent 50%);
  }
  .stage-art {
    position: absolute; top: 440px; left: 0; width: 900px; height: 560px;
    background:
      radial-gradient(ellipse 430px 210px at 450px 360px, rgba(255,130,60,.35), transparent 75%),
      radial-gradient(ellipse 380px 160px at 450px 200px, rgba(255,60,120,.3), transparent 75%),
      linear-gradient(180deg, rgba(90,10,50,.3) 0%, rgba(150,30,60,.45) 55%, rgba(40,10,60,.55) 85%, transparent 100%);
  }
  .stage-lines { position: absolute; top: 0; left: 0; }
  .logo-slot {
    position: absolute; left: 282px; top: 512px; width: 336px; height: 410px;
    border-radius: 40px;
    background: radial-gradient(ellipse at 50% 45%, rgba(255,255,255,.95) 0%, rgba(255,255,255,.8) 45%, rgba(255,240,255,.35) 80%, rgba(255,255,255,0) 100%);
    box-shadow: 0 0 40px rgba(255,255,255,.35);
  }
  .presenter {
    position: absolute; top: 98px; left: 0; right: 0;
    font-family: 'Great Vibes', cursive;
    font-size: 52px; line-height: 1; font-weight: 400;
    color: #fff4e8;
    text-shadow: 0 0 3px #5a0a2a, 0 2px 0 #3a0820;
  }
  .presents {
    position: absolute; top: 174px; left: 0; right: 0;
    font-size: 22px; font-weight: 500; letter-spacing: 12px;
    padding-left: 12px; line-height: 1.4;
  }
  .title {
    position: absolute; top: 228px; left: 0; right: 0;
    font-family: 'Anton', sans-serif; font-weight: 400;
    font-size: 192px; line-height: 1; letter-spacing: 3px;
    background: linear-gradient(180deg, #6a2fc2 0%, #7a3fd0 25%, #3fd65a 45%, #9a3fe0 62%, #e02ee0 85%, #c91fd0 100%);
    -webkit-background-clip: text; background-clip: text;
    color: transparent;
    -webkit-text-stroke: 2px #ffe6ff;
    filter: drop-shadow(3px 3px 0 var(--neon-pink)) drop-shadow(-2px 0 0 #3ff0ff);
  }
  .year {
    position: absolute; top: 968px; left: 0; right: 0;
    font-size: 82px; font-weight: 800; line-height: 1; letter-spacing: -1px;
    background: linear-gradient(180deg, var(--silver-hi) 0%, #d8d8de 45%, var(--silver-lo) 55%, #f2f2f4 100%);
    -webkit-background-clip: text; background-clip: text;
    color: transparent;
    filter: drop-shadow(0 3px 2px rgba(0,0,0,.6));
  }
  .event-name {
    position: absolute; top: 1050px; left: 0; right: 0;
    font-size: 42px; font-weight: 800; line-height: 1;
    color: var(--lime);
  }
  .contact {
    position: absolute; top: 1102px; left: 0; right: 0;
    display: flex; justify-content: center; align-items: center; gap: 12px;
    font-size: 21px; font-weight: 600;
  }
  .contact-item { display: flex; align-items: center; gap: 8px; }
  .divider { width: 1px; height: 26px; background: rgba(255,255,255,.7); margin: 0 4px; }
  .social-dot { width: 20px; height: 20px; border-radius: 50%; background: var(--lime); }
</style>
</head>
<body>
  <main class="cover">
    <div class="spotlights"></div>

    <div class="stage-art" role="img" aria-label="Glowing star-shaped marquee stage with bulbs and reflective floor"></div>

    <svg class="stage-lines" width="900" height="1200" viewBox="0 0 900 1200" aria-hidden="true">
      <defs>
        <linearGradient id="ringGlow" x1="0" y1="0" x2="1" y2="0">
          <stop offset="0" stop-color="#b98cff"/>
          <stop offset="0.5" stop-color="#ffffff"/>
          <stop offset="1" stop-color="#3fe07a"/>
        </linearGradient>
      </defs>
      <path d="M185 880 A297 297 0 1 1 715 880" fill="none" stroke="url(#ringGlow)" stroke-width="10" opacity=".35"/>
      <path d="M185 880 A297 297 0 1 1 715 880" fill="none" stroke="url(#ringGlow)" stroke-width="3"/>
      <path d="M0 905 Q450 885 900 905" fill="none" stroke="#ff8a5a" stroke-width="3" opacity=".7"/>
      <path d="M0 985 Q450 900 900 985" fill="none" stroke="#ff7aa0" stroke-width="3" opacity=".5"/>
      <line x1="60" y1="740" x2="90" y2="905" stroke="#b050ff" stroke-width="5" opacity=".7"/>
      <line x1="840" y1="740" x2="810" y2="905" stroke="#b050ff" stroke-width="5" opacity=".7"/>
    </svg>

    <div class="logo-slot" role="img" aria-label="Studio logo: three girls silhouette, supplied by client"></div>

    <h2 class="presenter">The Velvet Sparrows Dance Factory</h2>
    <p class="presents">PRESENTS</p>
    <h1 class="title">LEGENDS</h1>

    <p class="year">2023</p>
    <p class="event-name">ANNUAL SHOWCASE</p>

    <footer class="contact">
      <span class="contact-item">
        <svg width="24" height="24" viewBox="0 0 24 24" aria-hidden="true">
          <g fill="none" stroke="#d6e31b" stroke-width="2">
            <circle cx="12" cy="12" r="10"/>
            <ellipse cx="12" cy="12" rx="4.5" ry="10"/>
            <line x1="2" y1="12" x2="22" y2="12"/>
          </g>
        </svg>
        www.VSDFstudios-demo.net
      </span>
      <span class="divider"></span>
      <span class="contact-item">
        Follow us
        <span class="social-dot" aria-label="Snapvale"></span>
        @VSDF
      </span>
    </footer>
  </main>
</body>
</html>
```